Wedding Brochure/Booklet for Fern & The Hare

We have the content and a previous attempt already. We just need some edits and then have a version we can email as a PDF and Print as a Booklet.

Any further improvements to the visual aspect would also be welcomed

Check out our website to see who we are www.fernandthehare.example

Target Market(s)

Couples!!!!

Industry/Entity Type

Wedding

Font styles to use
Sans Serif
Decorative
Script

Requirements
Must have
• Style
Nice to have
• Style & Elegance
Should not have
• Too bold or Bright Colours

```html
<!DOCTYPE html>
<html lang="en">
<head>
<meta charset="utf-8">
<title>Fern &amp; The Hare – Wedding Menu Spread</title>
<link href="https://fonts.googleapis.com/css2?family=Didact+Gothic&family=Great+Vibes&display=swap" rel="stylesheet">
<style>
  :root {
    --backdrop: #e7e4e1;
    --paper: #ffffff;
    --ink: #2b2b2b;
    --heading-ink: #1f1f1f;
    --script-ink: #a4a4a9;
    --blush: #f6c3c6;
    --blush-soft: #fbe4e5;
    --spine-shade: rgba(0, 0, 0, 0.06);
  }
  * { margin: 0; padding: 0; box-sizing: border-box; }
  html, body {
    width: 1200px; height: 1200px; overflow: hidden;
    background: var(--backdrop);
  }
  .spread {
    position: absolute; left: 20px; top: 189px;
    width: 1160px; height: 822px;
    background: var(--paper);
    box-shadow: 0 10px 30px rgba(0,0,0,0.18);
    font-family: "Didact Gothic", "Century Gothic", sans-serif;
    color: var(--ink);
  }
  .spine-shade {
    position: absolute; left: 580px; top: 0; width: 70px; height: 100%;
    background: linear-gradient(to right, var(--spine-shade), rgba(0,0,0,0));
  }
  .ornament { position: absolute; }
  .ornament--top { left: 370px; top: 0; width: 423px; height: 168px; }
  .ornament--bottom { left: 471px; top: 735px; width: 216px; height: 87px; }
  .page { position: absolute; top: 0; width: 580px; height: 100%; text-align: center; }
  .page--left { left: 0; }
  .page--right { left: 580px; }
  .section { position: absolute; left: 0; width: 100%; }
  .section-title {
    font-size: 18px; font-weight: 400; letter-spacing: 0.2px;
    color: var(--heading-ink); line-height: 1;
  }
  .menu-list { list-style: none; margin-top: 18px; }
  .menu-list li { font-size: 12.2px; line-height: 19px; white-space: nowrap; }
  .script-title {
    position: absolute; top: 62px; left: 0; width: 100%;
    font-family: "Great Vibes", cursive; font-size: 40px; font-weight: 400;
    color: var(--script-ink); line-height: 1;
  }
</style>
</head>
<body>
<main class="spread">
  <div class="spine-shade"></div>

  <svg class="ornament ornament--top" viewBox="0 0 423 168" role="img" aria-label="Blush pink lace filigree ornament hanging from the top of the spread">
    <path d="M0 0 H423 C400 12 370 18 340 30 C300 50 270 90 245 120 C230 140 220 155 211 168 C202 155 192 140 177 120 C152 90 123 50 83 30 C53 18 23 12 0 0 Z" fill="var(--blush-soft)"/>
    <path d="M70 0 H353 C320 25 290 55 265 90 C245 115 225 140 211 158 C197 140 177 115 157 90 C132 55 103 25 70 0 Z" fill="var(--blush)" opacity="0.5"/>
  </svg>

  <svg class="ornament ornament--bottom" viewBox="0 0 216 87" role="img" aria-label="Blush pink lace filigree ornament rising from the bottom of the spread">
    <path d="M0 87 C30 70 60 40 85 20 C95 10 103 3 108 0 C113 3 121 10 131 20 C156 40 186 70 216 87 Z" fill="var(--blush-soft)"/>
  </svg>

  <section class="page page--left">
    <h1 class="script-title">Canape’s</h1>

    <div class="section" style="top:153px">
      <h2 class="section-title">HARE COCKTAIL MENU</h2>
      <ul class="menu-list">
        <li>Spanish Manchego Cheese Croquettes, Chipotle</li>
        <li>Beef Shin Sliders, American Cheese, Relish &amp; Beetroot</li>
        <li>Fried Chicken, Jalapenos, Slaw, Soft Shell Taco</li>
        <li>Salmon &amp; Avocado Crostino</li>
        <li>Polenta, Buffelo Mozzarella, Roasted Bell Peppers, Salsa Verde</li>
        <li>Flash Fried Baby Calamari, Lemon, Parsley &amp; Sea Salt</li>
        <li>Grilled Chorizitos Dagwood Dogs</li>
        <li>Caprese Heirloom Tomato, Pecorino, Basil &amp; Balsamic Bruschetta</li>
        <li>Prawn Goyza, Soy, Coriander &amp; Shallot Oil</li>
        <li>Corned Wagyu, Ghost Chilli Pickles, Skordalia</li>
      </ul>
    </div>

    <div class="section" style="top:419px">
      <h2 class="section-title">FERN COCKTAIL MENU</h2>
      <ul class="menu-list">
        <li>Charred Scallops, Pea Puree, Morcilla</li>
        <li>Grilled Australian King Prawns, Lemon &amp; Parsley Butter</li>
        <li>Lobster Sandwiches, Iceberg, Avocado, Firebrand Mayo</li>
        <li>Grilled Morrocan Lamb Skewers, Chermoula</li>
        <li>Hierloom Tomato, Cows Curd Crostino</li>
        <li>Grass Fed Eye Fillet, Horseradish, Garlic Baguette</li>
        <li>Spanish Manchego Cheese Croquettes, Chipotle</li>
        <li>Beef Shin Sliders, American Cheese, Relish &amp; Beetroot</li>
        <li>Fried Chicken, Jalapenos, Slaw, Soft Shell Taco</li>
        <li>Salmon &amp; Avocado Crostino</li>
        <li>Polenta, Buffelo Mozzarella, Roasted Bell Peppers, Salsa Verde</li>
        <li>Flash Fried Baby Calamari, Lemon, Parsley &amp; Sea Salt</li>
        <li>Grilled ChorizitosDagwood Dogs</li>
        <li>Twice Cooked Berkshire Pork Belly, Ginger &amp;Chilli Caramel, Fried Onion &amp; Coriander</li>
        <li>Caprese Heirloom Tomato, Pecorino, Basil &amp; Balsamic Bruschetta</li>
        <li>Prawn Goyza, Soy, Coriander&amp; Shallot OilCorned Wagyu, Ghost Chilli Pickles, Skordalia</li>
      </ul>
    </div>
  </section>

  <section class="page page--right">
    <div class="section" style="top:166px">
      <h2 class="section-title">DINNER MENU</h2>
      <ul class="menu-list">
        <li>Duck Maryland, Potato &amp; Leek Rostii, Orange Glaze GF</li>
        <li>Grass Fed Beef Fillet Tenderloin, Duck Fat Potatoes, Sauteed Mushrooms, Shiraz Jus</li>
        <li>Seared Sashimi Tuna, Mango &amp; Nashi Pear Salsa, Lime Vinaigrette</li>
        <li>Twice Cooked Master Stock Duck Breast, Sticky Black Rice, Ginger &amp; Shallot Dressing</li>
        <li>Roasted Barramundi, Wombok, Pinenuts, Fragrant Rice, Yellow Curry Sauce</li>
        <li>Fresh White Fish, Prawn &amp; Black Mussel Bisque, Potato Rouille, Garlic Bread</li>
        <li>Chargrilled Beef King Rib, Hassleback Potatoes, Truss Tomato &amp; Mustard Herb Butter</li>
        <li>Roasted Chicken Supreme, Prawn Stuffing, Spinach&amp;Pinenut Risotto, Thyme Jus</li>
        <li>Sticky Braised Pork Belly, Potato Gallette, Caramelised Apples</li>
        <li>Roasted Lamb Rump, Pistacio Crust, Pommes Dauphinaise, Rosemary Jus</li>
        <li>Veal Saltimboca, Proscuitto, Sage, Lemon and Paris Mash</li>
        <li>Herb Crumbed Pork Cutlet, LyonaissePototoes, Broccolini&amp; Thyme Jus</li>
        <li>Roasted Kent Pumpkin, Mint Crumb, Quinoa Tabouli, Lemon Yoghurt</li>
        <li>Grilled Lebanese Zucchini, Hummus, Chickpeas &amp; Pita</li>
        <li>Confit Mushrooms with Spinach &amp;PinenutPilaf, Willowbrook Goats’ Cheese Fetta</li>
      </ul>
    </div>

    <div class="section" style="top:531px">
      <h2 class="section-title">FERN &amp; THE HARE BEVERAGE PACKAGE</h2>
      <ul class="menu-list" style="margin-top:14px">
        <li>Beer – Harbourline Premium</li>
        <li>White – Stone Ridge “Grey Mare” Rhone Field Blend</li>
        <li>Red – Stone Ridge “Grey Mare” Shiraz, Sangiovese</li>
        <li>Sparkling – Stone Ridge NV Pinot Noir Pink</li>
        <li>Juice, Softdrinks&amp; Mineral Water</li>
      </ul>
    </div>
  </section>
</main>
</body>
</html>
```